High-end residential home builder needs a business card design

We need a new business card design for a small residential construction company based in Boise, Idaho. We specialize in building custom high-end homes and remodels, with a focus on great design and craftsmanship.

We would like to use our current logo, but open to new color suggestions.
Just looking for a clean, sharp, modern design that looks high-end.

Target Market(s)

Upscale clientele

Industry/Entity Type

Contractor

Contact Information for Business Card

Company: Stonefield Custom Builders
Name: Marcus Tilley
Phone number: 208 367 4120
Email: MarcusTilleySCB@mailbox-example.com
Website: Stonefieldcustombuilders-example.com

Font styles to use
Serif
Sans Serif

Requirements
Must have
• Company Logo
Company name
My name
My phone number
My email
Company website
Nice to have
• I have attached a few photos of cards that I really like.

```html
<!DOCTYPE html>
<html lang="en">
<head>
<meta charset="utf-8">
<title>Stonefield Custom Builders – Business Card</title>
<link rel="stylesheet" href="https://fonts.googleapis.com/css2?family=Montserrat:wght@400;500;700&display=swap">
<style>
  :root {
    --stage: #121213;
    --card: #2b2b2c;
    --ink: #ffffff;
    --ink-soft: #b9b9b9;
    --rule: #7a7a7a;
    --icon: #8c8c8c;
  }
  * { margin: 0; padding: 0; box-sizing: border-box; }
  html, body { width: 1200px; height: 1091px; overflow: hidden; }
  body {
    background: var(--stage);
    font-family: "Montserrat", Arial, sans-serif;
    color: var(--ink);
    position: relative;
  }
  .card {
    position: absolute;
    left: 100px;
    width: 1000px;
    height: 440px;
    background: var(--card);
    border-radius: 14px;
    overflow: hidden;
  }
  .card--front { top: 70px; }
  .card--back { top: 570px; }

  .card__strip {
    position: absolute;
    left: 0; right: 0; bottom: 34px;
    height: 5px;
    background: var(--rule);
  }
  .card__strip-mark {
    position: absolute;
    left: 46px; bottom: 26px;
    width: 20px; height: 20px;
    background: var(--card);
    border: 2px solid var(--ink);
  }

  /* front */
  .brand {
    position: absolute;
    left: 0; right: 0; top: 150px;
    display: flex;
    align-items: center;
    justify-content: center;
    gap: 30px;
  }
  .brand__square {
    width: 110px; height: 110px;
    border: 5px solid var(--ink);
  }
  .brand__name {
    font-weight: 500;
    font-size: 30px;
    letter-spacing: 7px;
    line-height: 1.35;
    text-transform: uppercase;
    color: var(--ink);
  }

  /* back */
  .back-brand {
    position: absolute;
    left: 70px; top: 0; bottom: 40px;
    width: 350px;
    display: flex;
    flex-direction: column;
    align-items: center;
    justify-content: center;
    gap: 22px;
  }
  .back-brand__square {
    width: 150px; height: 150px;
    border: 7px solid var(--ink);
  }
  .back-brand__name {
    font-weight: 500;
    font-size: 20px;
    letter-spacing: 5px;
    text-align: center;
    text-transform: uppercase;
    color: var(--ink);
  }
  .divider {
    position: absolute;
    left: 470px; top: 110px;
    width: 1px; height: 200px;
    background: var(--rule);
  }
  .person {
    position: absolute;
    left: 520px; top: 110px;
  }
  .person__name {
    font-weight: 700;
    font-size: 38px;
    letter-spacing: 2px;
    text-transform: uppercase;
  }
  .person__company {
    margin-top: 4px;
    font-size: 16px;
    letter-spacing: 1px;
    text-transform: uppercase;
    color: var(--ink-soft);
  }
  .contacts { list-style: none; margin-top: 22px; }
  .contacts__item {
    display: flex;
    align-items: center;
    gap: 16px;
    font-size: 17px;
    margin-bottom: 12px;
  }
  .contacts__item--phone { font-weight: 700; }
  .contacts__icon { width: 26px; height: 22px; flex: none; }
</style>
</head>
<body>
  <section class="card card--front">
    <div class="brand">
      <div class="brand__square"></div>
      <div class="brand__name">Stonefield<br>Custom Builders</div>
    </div>
    <div class="card__strip"></div>
    <div class="card__strip-mark"></div>
  </section>

  <section class="card card--back">
    <div class="back-brand">
      <div class="back-brand__square"></div>
      <div class="back-brand__name">Stonefield<br>Custom Builders</div>
    </div>
    <div class="divider"></div>
    <div class="person">
      <h1 class="person__name">Marcus Tilley</h1>
      <p class="person__company">Stonefield Custom Builders</p>
      <ul class="contacts">
        <li class="contacts__item contacts__item--phone">
          <svg class="contacts__icon" viewBox="0 0 26 22" fill="none" stroke="var(--icon)" stroke-width="2">
            <path d="M3 8 Q13 1 23 8 L21 11 L17 9 L17 7 Q13 5 9 7 L9 9 L5 11 Z"/>
            <rect x="6" y="12" width="14" height="8" rx="2"/>
          </svg>
          208 367 4120
        </li>
        <li class="contacts__item">
          <svg class="contacts__icon" viewBox="0 0 26 22" fill="none" stroke="var(--icon)" stroke-width="2">
            <rect x="2" y="4" width="22" height="14"/>
            <path d="M2 4 L13 12 L24 4"/>
          </svg>
          MarcusTilleySCB@mailbox-example.com
        </li>
        <li class="contacts__item">
          <svg class="contacts__icon" viewBox="0 0 26 22" fill="none" stroke="var(--icon)" stroke-width="2">
            <circle cx="13" cy="11" r="9"/>
            <ellipse cx="13" cy="11" rx="4" ry="9"/>
            <path d="M4 11 H22"/>
          </svg>
          Stonefieldcustombuilders-example.com
        </li>
      </ul>
    </div>
    <div class="card__strip"></div>
    <div class="card__strip-mark"></div>
  </section>
</body>
</html>
```